" Prestando serviços especializados de advocacia, em especial nas áreas de Direito médico, terceiro setor e responsabilidade civil em virtude de acidente de trânsito "

```html
<!DOCTYPE html>
<html lang="pt-BR">
<head>
<meta charset="utf-8">
<title>Papel timbrado – Ferraz Mendonça Advogados Associados</title>
<link href="https://fonts.googleapis.com/css2?family=Lato:wght@400;700&display=swap" rel="stylesheet">
<style>
  :root {
    --backdrop: #e9e7e3;
    --paper: #ffffff;
    --gold: #b07a2a;
    --gold-dark: #8a5a17;
    --gray-band: #c9c9c9;
    --ink: #3b3b3b;
    --ink-soft: #6b6b6b;
    --signature-a: #d9d9de;
    --signature-b: #b9b9c2;
  }
  * { box-sizing: border-box; margin: 0; padding: 0; }
  html, body { width: 1200px; height: 1200px; overflow: hidden; }
  body {
    background: var(--backdrop);
    font-family: "Lato", Arial, sans-serif;
    color: var(--ink);
  }
  .letterhead {
    position: absolute;
    left: 211px; top: 50px;
    width: 778px; height: 1100px;
    background: var(--paper);
    box-shadow: 0 6px 24px rgba(0,0,0,.12);
    overflow: hidden;
  }
  .letterhead__bands { position: absolute; inset: 0; width: 100%; height: 100%; }
  .brand {
    position: absolute; left: 70px; top: 150px;
    display: flex; align-items: center; gap: 14px;
  }
  .brand__dot { width: 26px; height: 26px; border-radius: 50%; background: var(--gold); }
  .brand__name {
    font-weight: 700; color: var(--gold);
    font-size: 22px; line-height: 1.05; text-transform: uppercase; letter-spacing: .5px;
  }
  .brand__name small { display: block; font-size: 9px; letter-spacing: 2px; margin-top: 3px; }
  .letter {
    position: absolute; left: 70px; top: 300px; width: 620px;
    font-size: 12px; line-height: 1.6; color: var(--ink-soft);
  }
  .letter__to { margin-bottom: 26px; color: var(--ink); }
  .letter p { margin-bottom: 28px; }
  .closing {
    position: absolute; left: 520px; top: 640px; width: 180px;
    font-size: 10px; color: var(--ink-soft);
  }
  .closing__signature {
    display: block; margin-top: 8px; width: 80px; height: 42px;
    background: linear-gradient(135deg, var(--signature-a), var(--signature-b));
    border-radius: 4px;
  }
  .contact {
    position: absolute; right: 70px; bottom: 70px;
    text-align: right; font-size: 10px; line-height: 1.55; color: var(--ink-soft);
  }
</style>
</head>
<body>
  <main class="letterhead">
    <svg class="letterhead__bands" viewBox="0 0 778 1100" aria-hidden="true">
      <path d="M560 0 Q 650 40 778 140 L778 0 Z" fill="var(--gold)"/>
      <path d="M600 0 Q 690 30 778 110 L778 0 Z" fill="var(--gold-dark)" opacity=".35"/>
      <path d="M0 960 Q 90 1030 150 1100 L0 1100 Z" fill="var(--gray-band)"/>
    </svg>

    <header class="brand">
      <span class="brand__dot"></span>
      <div class="brand__name">Ferraz<br>Mendonça<small>Advogados Associados</small></div>
    </header>

    <section class="letter">
      <p class="letter__to">A/C Nome do Responsável</p>
      <p>Prezados, apresentamos nossa proposta de atuação jurídica especializada, com atendimento próximo, análise criteriosa de cada caso e acompanhamento integral dos processos em todas as instâncias, buscando soluções seguras e eficientes para nossos clientes.</p>
      <p>Nossa equipe atua em direito médico, terceiro setor e responsabilidade civil decorrente de acidentes de trânsito, sempre com ética, transparência e dedicação a cada demanda apresentada.</p>
      <p>Permanecemos à disposição para esclarecer dúvidas, agendar reuniões e apresentar os documentos necessários. Agradecemos a atenção e a confiança depositada em nosso escritório, certos de uma parceria duradoura e produtiva.</p>
    </section>

    <aside class="closing">
      <span>Atenciosamente</span>
      <span class="closing__signature" role="img" aria-label="Assinatura manuscrita do advogado responsável"></span>
    </aside>

    <footer class="contact">
      Rua das Palmeiras, 480 / Jardim Aurora<br>
      Vila Serena - SP<br>
      (11) 4002-7719<br>
      contato@ferrazmendonca.adv.br<br>
      www.ferrazmendonca.adv.br
    </footer>
  </main>
</body>
</html>
```